依頼詳細
ホームページのロゴを使いたいです。デリケートな問題ですが、事前に考え、ぜひ終活のお話をきき、
エンディングノートを一緒に書きたくなるような内容。H25年11月、9,10日の産業祭や、ポスティングで使います。
ですが、そこから繋がりができ、御葬儀の依頼をふやしたいです。
終活のイメージは、ホームページのブログの手と手を繋ぐ絵でお願したいです。
記載項目
あおば典礼(ロゴ) キャッチコピー 『大切な人を見送る方々とともに・・・まごころをこめて・・・』
〒317-0088 茨城県日立市緑苑町8-27-3
電話0294-58-7261 FAX0294-43-3540
ホームページ、あおば典礼 検索 フェイスブックページ
御葬儀の内容、金額等
終活相談会の実施、個別、グループで依頼、場所は御自宅、集会所、あおば典礼事務所でも定期的に実施しています。(ホームページ内ブログ、フェイスブックページ、事務所外掲示板、お電話にてご確認下さい。
サイズ
A4
ページ数
両面
希望イメージ
シンプル 複雑
単色 カラフル
暗い 明るい
日常 高級
遊び心 厳粛
未来的 伝統的
女性的 男性的
希望する色
紫、ピンク、
納品ファイル
• 高解像度JPG (.jpg)
補足説明
あおば典礼のホームページ参考にして下さい。
お世話になります。
終活と、御葬儀の宣伝も入れて下さい。

toriyoshiさんの提案は、お葬儀の事と、終活のこと、会社の売り、私どもの気持ちを汲んだ内容が、よくホームページやファイルを読み込んでくれていたと思いました。

お世話になりました。
初めての依頼で要領が分からず、提案しずらかったと思います。
沢山の提案をいただき、自分達が気づかなかった会社の特徴も分かりました。
lanternflyさんには、質問していただいた内容に、すぐに対応して
修正した提案をあげてもらい、ありがたい気持ちです。
会員様へ送っている、瓦版でしたらlanternflyさんの提案が親近感あってよかったと思います。皆さん、きれいに仕上げてくださり ありがとうございました。
また、何か機会がありましたら その時は宜しくお願い申しあげます。

```html
<!DOCTYPE html>
<html lang="ja">
<head>
<meta charset="utf-8">
<title>あおば典礼 終活セミナーのご案内</title>
<link rel="stylesheet" href="https://fonts.googleapis.com/css2?family=Shippori+Mincho+B1:wght@600;800&family=Noto+Sans+JP:wght@400;500;700&family=Noto+Serif+JP:wght@500;700&display=swap">
<style>
:root{
  --purple:#6b3f86;
  --purple-deep:#4f2a66;
  --lilac:#efe6f3;
  --pink:#e0427a;
  --ink:#222;
  --white:#fff;
}
*{margin:0;padding:0;box-sizing:border-box}
html,body{width:849px;height:1200px;overflow:hidden;background:var(--white)}
body{font-family:"Noto Sans JP",sans-serif;color:var(--ink)}
.flyer{position:relative;width:849px;height:1200px;overflow:hidden;background:var(--white)}
.hero{position:absolute;left:0;top:0;width:849px;height:345px;
  background:radial-gradient(ellipse at 20% 30%,#f9e9ef 0%,transparent 55%),
             radial-gradient(ellipse at 80% 60%,#efd4df 0%,transparent 60%),
             linear-gradient(180deg,#e8cfd9 0%,#f7ebf0 55%,#ffffff 100%)}
.tagline{position:absolute;left:0;top:12px;width:849px;text-align:center;
  font-family:"Noto Serif JP",serif;font-size:22px;letter-spacing:4px;color:var(--white);
  text-shadow:0 0 6px rgba(120,60,90,.55)}
.brand{position:absolute;left:250px;top:130px;display:flex;align-items:center;gap:18px}
.brand-dot{width:70px;height:70px;border-radius:50%;background:var(--pink)}
.brand-name{font-family:"Shippori Mincho B1",serif;font-weight:800;font-size:66px;color:var(--purple-deep);letter-spacing:4px}
.headline{position:absolute;left:58px;top:352px;font-family:"Shippori Mincho B1",serif;font-weight:800;
  font-size:37px;line-height:54px;color:var(--ink);white-space:nowrap}
.headline .key{color:var(--pink);font-size:44px}
.checklist{position:absolute;left:58px;top:540px;display:grid;grid-template-columns:108px 140px 150px;
  row-gap:14px;font-size:16px;font-weight:500;white-space:nowrap}
.checklist li{list-style:none}
.checklist li::before{content:"■";color:var(--purple);margin-right:3px}
.intro{position:absolute;left:58px;top:722px;width:450px;font-size:14px;line-height:22px}
.intro em{font-style:normal;color:var(--pink)}
.note{position:absolute;left:58px;top:818px;width:450px;font-size:12px;line-height:18px;color:var(--pink)}
.circle-art{position:absolute;left:515px;top:510px;width:320px;height:320px;border-radius:50%;
  background:radial-gradient(circle,#fbe7ef 0%,#f3c6d6 60%,#e7a9c0 100%)}
.seminar{position:absolute;left:46px;top:882px;width:757px;height:306px;border:3px solid var(--purple);background:var(--white)}
.seminar-head{height:40px;background:var(--lilac);border-bottom:2px solid var(--purple);display:flex;align-items:center;gap:12px;padding-left:14px;
  font-family:"Noto Serif JP",serif;font-weight:700;font-size:22px;color:var(--purple-deep)}
.free{background:var(--pink);color:var(--white);font-family:"Noto Sans JP",sans-serif;font-size:15px;padding:0 8px;line-height:24px}
.seminar-text{padding:10px 18px 0;font-size:15px;line-height:24px}
.contact{display:flex;align-items:center;gap:10px;padding:4px 18px 0;color:var(--purple-deep);font-weight:700;white-space:nowrap;height:62px}
.contact .label{background:var(--purple);color:var(--white);font-size:18px;padding:0 8px;line-height:28px}
.contact .num{font-size:42px;line-height:56px;margin-right:26px}
.contact .num.fax{font-size:34px}
.links{padding:4px 18px 0;font-size:15px}
.links .row{display:flex;align-items:center;gap:12px;height:32px;white-space:nowrap}
.links .tag{background:var(--purple);color:var(--white);font-size:12px;line-height:20px;width:96px;text-align:center;white-space:nowrap}
.search{position:absolute;right:18px;bottom:48px;display:flex;white-space:nowrap}
.search .box{border:2px solid var(--purple);padding:2px 16px;font-size:17px;color:var(--purple-deep);font-weight:700}
.search .btn{background:var(--purple);color:var(--white);padding:4px 12px;font-size:16px}
</style>
</head>
<body>
<div class="flyer">
  <div class="hero" role="img" aria-label="満開の桜の花を下から見上げた淡いピンクの写真"></div>
  <p class="tagline">大切な人を 見送る方々とともに まごころをこめて…</p>
  <div class="brand"><span class="brand-dot"></span><span class="brand-name">あおば典礼</span></div>

  <h1 class="headline">自分らしいエンディングを考え<br>大切な方へ、そして自分のために<br>『ありがとう』を伝える活動が <span class="key">終活</span> です。</h1>

  <ul class="checklist">
    <li>終の棲家</li><li>臓器提供の有無</li><li>延命処置の有無</li>
    <li>自分の記録</li><li>親族の記録</li><li>形見分けリスト</li>
    <li>葬儀の希望</li><li>など…</li>
  </ul>

  <p class="intro">これからの人生を有意義に活力あるものにしていくために、明るい気持ちで、一つ一つ自分の想いを<em>エンディングノート</em>に記しておくのはいかがですか？<br><em>エンディングノート</em>はあおば典礼にございます。</p>
  <p class="note">生きた手を次の世代へつなぐために、終活サポーターの活動を通して、地域の皆様のお役に立てるよう努めてまいります。どうぞお気軽にご相談ください。</p>

  <div class="circle-art" role="img" aria-label="桜の花を囲んで手をつなぐ人々の円形イラスト"></div>

  <section class="seminar">
    <div class="seminar-head">終活セミナー(相談会)<span class="free">無料</span></div>
    <p class="seminar-text">個別・グループで依頼、お電話にて日時ご予約下さい。<br>場所は御自宅、集会所、あおば典礼事務所でも定期的に実施しています。<br>(ホームページ内ブログ、フェイスブックページ、事務所外掲示板、お電話にてご確認下さい)</p>
    <div class="contact"><span class="label">TEL</span><span class="num">0294-58-7261</span><span class="label">FAX</span><span class="num fax">0294-58-7269</span></div>
    <div class="links">
      <div class="row"><span class="tag">ホームページ</span>http://www.aoba-tenrei.jp/</div>
      <div class="row"><span class="tag">フェイスブック</span>https://www.facebook.com/AobaTenrei</div>
    </div>
    <div class="search"><span class="box">あおば典礼</span><span class="btn">検索</span></div>
  </section>
</div>
</body>
</html>
```